Stationery Design Project

I am looking for stationary design for an automotive collision repair company. This needs to work with my business cards just designed here. I've attached. I need 8.5 x 11 stationary and corissponding envelopes. a post it note pad also. Our companies focus is very high end customer service driven . Our customer base is 35-65 middle to high income. Please include company name, logo, address, phone number, web address. The business card is two greys with green and white writing. I invision a light grey background with a darker grey band on it that contains the logo.

I justĀ 

Why is no one touching this project

Target Market(s)

60%. Women 40% men. Age 35-60

Industry/Entity Type

Automotive

Requirements
Must have
• Tie in with business cards. So it needs grey tones with green and white logo. Name, address, phone and web address. Must have 8.5 x 11 paper and envelopes.
Nice to have
• Post it notes

```html
<!DOCTYPE html>
<html lang="en">
<head>
<meta charset="utf-8">
<title>Apexline Auto — Stationery</title>
<link rel="stylesheet" href="https://fonts.googleapis.com/css2?family=Arimo:wght@400;700&display=swap">
<style>
  :root {
    --backdrop: #f3f3f3;
    --paper: #ececec;
    --paper-edge: #dcdcdc;
    --green-light: #cdf27e;
    --green-mid: #8cc63f;
    --green-deep: #4f8a1c;
    --flap: #7db335;
    --ink-white: #ffffff;
    --ink-dark: #2f4a12;
    --brand: #6fae2a;
  }
  * { box-sizing: border-box; margin: 0; padding: 0; }
  html, body {
    width: 1154px; height: 1200px; overflow: hidden;
    background: var(--backdrop);
    font-family: "Arimo", Arial, sans-serif;
  }
  .canvas { position: relative; width: 1154px; height: 1200px; }
  .sheet {
    position: absolute; background: var(--paper);
    border: 1px solid var(--paper-edge); overflow: hidden;
  }
  .wave { position: absolute; left: 0; bottom: 0; width: 100%; display: block; }
  .brand {
    position: absolute; color: var(--brand); font-weight: 700;
    white-space: nowrap; letter-spacing: 0.2px;
  }
  .contact { position: absolute; color: var(--ink-dark); line-height: 1.3; }
  .contact .company { color: var(--ink-white); font-size: 19px; letter-spacing: 0.5px; margin-bottom: 3px; }
  .contact p { font-size: 8px; }

  .letterhead-front { left: 109px; top: 79px; width: 456px; height: 585px; }
  .letterhead-front .brand { left: 22px; top: 42px; font-size: 14px; }
  .letterhead-front .wave { height: 112px; }
  .letterhead-front .contact { left: 322px; top: 522px; }

  .letterhead-back { left: 602px; top: 79px; width: 456px; height: 578px; }
  .letterhead-back .brand { left: 0; right: 0; top: 527px; text-align: center; font-size: 17px; }

  .envelope-front { left: 108px; top: 738px; width: 457px; height: 192px; }
  .envelope-front .brand { right: 28px; top: 24px; font-size: 13px; }
  .envelope-front .wave { height: 82px; }
  .envelope-front .contact { left: 342px; top: 148px; }
  .envelope-front .contact p { font-size: 7px; }

  .envelope-back { left: 599px; top: 738px; width: 459px; height: 192px; }
  .envelope-back .flap {
    position: absolute; left: 0; top: 0; width: 100%; height: 47px;
    background: var(--flap); border-radius: 0 0 16px 16px;
  }
  .envelope-back .brand { right: 22px; top: 152px; font-size: 13px; }

  .note { left: 318px; top: 990px; width: 176px; height: 170px; }
  .note .corner { position: absolute; left: 0; bottom: 0; width: 70px; height: 46px; display: block; }
  .note .brand { right: 14px; bottom: 26px; font-size: 10px; }

  .notepad { left: 672px; top: 1000px; width: 186px; height: 172px; border-left: 8px solid #c9c9c9; }
  .notepad .brand { right: 14px; bottom: 20px; font-size: 10px; }
</style>
</head>
<body>
<main class="canvas">

  <section class="sheet letterhead-front" aria-label="Letterhead, front">
    <span class="brand">Apexline Auto</span>
    <svg class="wave" viewBox="0 0 456 112" preserveAspectRatio="none" aria-hidden="true">
      <defs>
        <linearGradient id="lhGreen" x1="0" y1="0" x2="0" y2="1">
          <stop offset="0" stop-color="#8cc63f"/>
          <stop offset="1" stop-color="#4f8a1c"/>
        </linearGradient>
      </defs>
      <path d="M0 20 C80 8 160 20 250 26 C340 32 410 22 456 0 L456 112 L0 112 Z" fill="var(--green-light)"/>
      <path d="M0 58 C120 40 260 60 340 36 C400 20 440 14 456 10 L456 112 L0 112 Z" fill="url(#lhGreen)"/>
    </svg>
    <div class="contact">
      <div class="company">Apexline Auto</div>
      <p>48 Harrow Lane, Leeds</p>
      <p>office: 0113 555 0192</p>
      <p>web: www.apexlineauto.com</p>
      <p>e-mail: hello@apexlineauto.com</p>
    </div>
  </section>

  <section class="sheet letterhead-back" aria-label="Letterhead, second page">
    <span class="brand">Apexline Auto</span>
  </section>

  <section class="sheet envelope-front" aria-label="Envelope, front">
    <span class="brand">Apexline Auto</span>
    <svg class="wave" viewBox="0 0 457 82" preserveAspectRatio="none" aria-hidden="true">
      <defs>
        <linearGradient id="envGreen" x1="0" y1="0" x2="0" y2="1">
          <stop offset="0" stop-color="#8cc63f"/>
          <stop offset="1" stop-color="#4f8a1c"/>
        </linearGradient>
      </defs>
      <path d="M0 14 C90 4 180 18 270 20 C360 22 420 12 457 0 L457 82 L0 82 Z" fill="var(--green-light)"/>
      <path d="M0 42 C120 30 250 46 340 26 C400 14 440 10 457 8 L457 82 L0 82 Z" fill="url(#envGreen)"/>
    </svg>
    <div class="contact">
      <p>48 Harrow Lane, Leeds</p>
      <p>office: 0113 555 0192</p>
      <p>web: www.apexlineauto.com</p>
      <p>e-mail: hello@apexlineauto.com</p>
    </div>
  </section>

  <section class="sheet envelope-back" aria-label="Envelope, back">
    <div class="flap"></div>
    <span class="brand">Apexline Auto</span>
  </section>

  <section class="sheet note" aria-label="Sticky note">
    <svg class="corner" viewBox="0 0 70 46" preserveAspectRatio="none" aria-hidden="true">
      <path d="M0 0 C20 10 40 20 56 30 C62 36 66 42 70 46 L0 46 Z" fill="var(--green-mid)"/>
    </svg>
    <span class="brand">Apexline Auto</span>
  </section>

  <section class="sheet notepad" aria-label="Note pad">
    <span class="brand">Apexline Auto</span>
  </section>

</main>
</body>
</html>
```